Halvorsen Plumbing LLC business card

Would like a modern looking business card with my new logo

Contact Information for Business Card

Dwight Halvorsen 2417 Birchmont Hollow Rd Southbury, CT 06512, Halvorsenplumbingllc@mailnest.example, 203-555-0184

```html
<!DOCTYPE html>
<html lang="en">
<head>
<meta charset="utf-8">
<title>Halvorsen Plumbing LLC business card</title>
<link href="https://fonts.googleapis.com/css2?family=Arimo:wght@400;700&display=swap" rel="stylesheet">
<style>
  :root {
    --page: #e6e6e4;
    --card: #2b2b30;
    --card-deep: #1f1f23;
    --blue: #0ba4e2;
    --white: #ffffff;
    --rule: #9a9aa0;
  }
  * { box-sizing: border-box; margin: 0; padding: 0; }
  html, body { width: 1200px; height: 801px; overflow: hidden; }
  body {
    background: var(--page);
    font-family: "Arimo", Arial, sans-serif;
    position: relative;
  }
  .card {
    position: absolute;
    top: 246px;
    width: 540px;
    height: 309px;
    background: var(--card);
    overflow: hidden;
    box-shadow: 0 6px 18px rgba(0,0,0,0.18);
  }
  .card--front { left: 40px; }
  .card--back { left: 620px; }

  /* front */
  .brand-name {
    position: absolute;
    color: var(--white);
    font-weight: 700;
    letter-spacing: 1px;
    text-transform: uppercase;
    line-height: 1.05;
  }
  .card--front .brand-name {
    right: 34px; top: 34px;
    font-size: 24px;
    text-align: right;
  }
  .brand-name small {
    display: block;
    font-size: 0.55em;
    letter-spacing: 3px;
    margin-top: 4px;
  }
  .brand-rule {
    position: absolute;
    right: 34px; top: 106px;
    width: 220px; height: 2px;
    background: var(--white);
  }
  .divider {
    position: absolute;
    left: 256px; right: 20px; top: 206px;
    height: 1px;
    background: var(--rule);
  }
  .address {
    position: absolute;
    right: 34px; top: 218px;
    color: var(--white);
    font-size: 13px;
    line-height: 1.35;
    text-align: left;
  }
  .holder {
    position: absolute;
    left: 30px; top: 178px;
    color: var(--blue);
    font-size: 19px;
    font-weight: 400;
    text-transform: uppercase;
    letter-spacing: 0.5px;
    line-height: 1.2;
  }
  .holder-rule {
    position: absolute;
    left: 30px; top: 206px;
    width: 210px; height: 1px;
    background: var(--rule);
  }
  .contact-list {
    position: absolute;
    left: 30px; top: 218px;
    list-style: none;
    color: var(--white);
    font-size: 13px;
  }
  .contact-list li {
    display: flex;
    align-items: center;
    gap: 8px;
    margin-bottom: 8px;
  }
  .contact-list svg { width: 13px; height: 13px; flex: none; }
  .accent-band {
    position: absolute;
    left: 0; right: 0; bottom: 0;
    height: 8px;
    background: var(--blue);
  }

  /* back */
  .pipe-art {
    position: absolute;
    right: 0; top: 0;
    width: 250px; height: 309px;
    background: linear-gradient(135deg, var(--card) 10%, var(--card-deep) 50%, #55555b 100%);
  }
  .card--back .brand-name {
    left: 70px; top: 118px;
    font-size: 36px;
  }
  .card--back .brand-rule {
    right: auto; left: 70px; top: 200px;
    width: 300px;
  }
</style>
</head>
<body>
  <section class="card card--front">
    <div class="brand-name">Halvorsen<small>Plumbing LLC</small></div>
    <div class="brand-rule"></div>
    <h1 class="holder">Dwight Halvorsen</h1>
    <div class="holder-rule"></div>
    <div class="divider"></div>
    <p class="address">2417 Birchmont Hollow Rd<br>Southbury, CT 06512</p>
    <ul class="contact-list">
      <li>
        <svg viewBox="0 0 24 24" aria-hidden="true"><path fill="#0ba4e2" d="M6.6 10.8a15.1 15.1 0 0 0 6.6 6.6l2.2-2.2c.3-.3.7-.4 1-.2 1.1.4 2.3.6 3.6.6.6 0 1 .4 1 1V20c0 .6-.4 1-1 1A17 17 0 0 1 3 4c0-.6.4-1 1-1h3.5c.6 0 1 .4 1 1 0 1.3.2 2.5.6 3.6.1.3 0 .7-.2 1z"/></svg>
        203-555-0184
      </li>
      <li>
        <svg viewBox="0 0 24 24" aria-hidden="true"><rect x="2" y="5" width="20" height="14" fill="#0ba4e2"/><path d="M2 5l10 8 10-8" fill="none" stroke="#2b2b30" stroke-width="2"/></svg>
        Halvorsenplumbingllc@mailnest.example
      </li>
    </ul>
    <div class="accent-band"></div>
  </section>

  <section class="card card--back">
    <div class="pipe-art" role="img" aria-label="Large embossed pipe fitting decoration in dark grey"></div>
    <div class="brand-name">Halvorsen<small>Plumbing LLC</small></div>
    <div class="brand-rule"></div>
  </section>
</body>
</html>
```